Lumo -Fresh business card design

It is a dry cleaning carpet business.
Red wine stain removal and pet urine treatments.
Servicing all regional areas.
Updates

all logo and pictures files have been uploaded

Industry/Entity Type

Dry Cleaning

Contact Information for Business Card

Lumo-Fresh Carpet and upholstery cleaning.
Servicing Brightvale/Tarrow and surrounding areas.
ph gus 0461273904 ,email lumofresh1@tealpost.example

Font styles to use
Serif
Sans Serif
Other font styles liked:
• lumo fresh logo font

Colors
ec2027
ffcf3e
33a6d7
0692cd

Requirements
Nice to have
• I have included photos of the logo and car and stripe on van ,I dont need all of them in the card just i would like to stick to these colours.

```html
<!DOCTYPE html>
<html lang="en">
<head>
<meta charset="utf-8">
<title>Lumo-Fresh Business Card</title>
<link rel="stylesheet" href="https://fonts.googleapis.com/css2?family=Arimo:wght@400;700&display=swap">
<style>
  :root {
    --bg: #3a3a3a;
    --card: #ffffff;
    --blue: #2a8fc4;
    --yellow: #f2c13f;
    --red: #e0343a;
    --ink: #1c1c1c;
    --muted: #4a4a4a;
  }
  html, body {
    margin: 0;
    width: 1200px;
    height: 821px;
    overflow: hidden;
    background: var(--bg);
  }
  .canvas {
    width: 1200px;
    height: 821px;
    display: flex;
    align-items: center;
    justify-content: center;
  }
  .card {
    position: relative;
    width: 900px;
    height: 540px;
    background: var(--card);
    box-shadow: 0 10px 30px rgba(0,0,0,0.35);
    font-family: "Arimo", Arial, sans-serif;
    overflow: hidden;
  }
  .stripe-band {
    position: absolute;
    top: 0;
    right: 0;
    width: 130px;
    height: 100%;
    display: flex;
    flex-direction: column;
  }
  .stripe-blue { flex: 0 0 58%; background: var(--blue); }
  .stripe-yellow { flex: 0 0 17%; background: var(--yellow); }
  .stripe-red { flex: 1; background: var(--red); }
  .brand {
    position: absolute;
    left: 70px;
    top: 120px;
  }
  .brand-name {
    margin: 0;
    font-size: 72px;
    font-weight: 700;
    color: var(--blue);
    letter-spacing: 2px;
    text-transform: uppercase;
    line-height: 1;
  }
  .tagline {
    margin: 12px 0 0 2px;
    font-size: 34px;
    font-weight: 700;
    color: var(--ink);
    text-transform: uppercase;
    line-height: 1.08;
  }
  .contact {
    position: absolute;
    left: 72px;
    bottom: 64px;
    font-size: 24px;
    color: var(--ink);
    line-height: 1.3;
  }
  .contact p { margin: 0; }
  .contact .label { color: var(--blue); }
  .contact .area {
    margin-top: 2px;
    font-size: 18px;
    color: var(--muted);
  }
</style>
</head>
<body>
<main class="canvas">
  <article class="card">
    <div class="stripe-band">
      <div class="stripe-blue"></div>
      <div class="stripe-yellow"></div>
      <div class="stripe-red"></div>
    </div>
    <header class="brand">
      <h1 class="brand-name">Lumo-Fresh</h1>
      <p class="tagline">Carpet &amp; Upholstery<br>Cleaning</p>
    </header>
    <section class="contact">
      <p><span class="label">P:</span> 0461 273 904</p>
      <p><span class="label">E:</span> lumofresh1@tealpost.example</p>
      <p class="area">Servicing Brightvale/Tarrow and surrounding areas</p>
    </section>
  </article>
</main>
</body>
</html>
```